Professional Lawn Treatment flyer (double sided) needed for established gardening company

We are an established and trusted gardening company in Swindon, UK, and are about to launch a new Lawn Treatment Service. This will be marketed to both existing and new customers and needs to reflect our current professional image. The flyer will need to be double-sided, portrait orientation and correctly sized so to be printed on A5.

If you look on our website www.pelhamgardening.co.uk, you will see our colours are purple and green. We would like you to use these exact shades of purple and green in your design.

As part of the design, we will need you to put together an infographic table to show our packages. I have attached a spreadsheet which explains these packages but I will need you to create a visually appealing table that fits in with the overall design of the flyer. I don't want you to simply cut and paste my basic table into the design.

In terms of what needs to be included, I have tried to be as specific as possible here but please feel free to message me if you need any further information or clarification.

FRONT SIDE:
The title of our service is:
Expert Lawn Treatment Service

Our strapline will need to be included somewhere:
"Lawn care by your local gardening expert"

The front side of the flyer will need to contain our logo - different versions of which can be found within my dropbox folder here...

https://www.filecrate.net/sh/k7bq24nwxe9/QWT8PmRzLxKd3VuYcH0BnJeFa?dl=0

The front side will need to contain a main image (although feel free to add more if you have anything suitable). I have included a picture in the dropbox folder titled "Front side image" which we would like used. I've also included in the folder an adobe image of grass which you may or may not like to use on either front or back.

Somewhere on both the front and back sides, you will need to include our contact details:
01632 960481
www.pelhamgardening.co.uk/lawncare

The front side should show what treatments we currently have available. These are:

- Lawn Fertilising
- Scarification
- Aeration
- Weed Control
- Moss Control
- Hydration Booster
- Kempix
- Turfing & Renovation

"Select a one-off treatment or choose from one of our specially created lawn care packages."

BACK SIDE:
On the back, we will still need our logo and contact details but the image we'd like used should be the one in the dropbox folder titled "Back side image". Again, if you have any other images you feel would also work, then please feel free to add them.

The back side is to contain a bit more information and be a bit 'wordier' and so can you please include the following 2 paragraphs:

"As expert gardeners, we are passionate about horticulture and working to bring out the very best in your garden. When we work in your garden, we look at it and treat it with the same care and attention as if it were our own, before handing it back for you to enjoy. Our passion doesn't end at just trees and shrubs though. Your grass is as much of a living, breathing plant as your shrubs and we therefore utilise our expert horticultural knowledge to ensure your lawn thrives and reaches its fullest potential.

Lawn care isn't just about applying a fertiliser. It's about really understanding your lawn and being able to use extensive knowledge and experience to diagnose and treat issues. It therefore stands to reason that you should employ an expert to bring out the best in your lawn which is why we at Pelham Gardening Services have created a superior lawn care service that will keep your lawn looking lush, green and healthy all year round."

I referred at the very top of this brief to the fact we will need an infographic table created to show the different lawn care packages available. You see from the PDF table I created that we have 3 packages; Standard, Enhanced and Premium. Please create a visually appealing table which sets out the differences between our packages and include it on the back page.

Finally, somewhere we would like reference to the other gardening services we do. It's only to be something small as it isn't the main focus of the flyer but we think it would be good to mention what else we do. To re-iterate, it isnt to be big. I still want the main focus to be lawn care but if you could somehow reference that we also do the following services, that would be good. I will leave it to you to decide where on the flyer it fits in best, be it the front or back:

- Lawn mowing
- Shrub pruning
- Hedge trimming
- Weed killing
- Garden clearance & tidy-up
- Planting & design
- Regular Garden Maintenance
- Turfing
- Fencing
- Gutter clearance

I think thats it. I look forward to your designs!
Ps. Don't forget the dropbox folder:

Target Market(s)

Professional men/women aged 25+
Retired aged 65+

Industry/Entity Type

Home And Garden

Font styles to use
Sans Serif

Colors
6b449b
9bcb3c

Requirements
Must have
• Our company colours; purple and green; as per our website www.pelhamgardening.co.uk. I've selected purple and green on this brief just to highlight the colours needed but please be sure to use the exact shades from our website and NOT the shade of purple and green that were selected on this brief.
• All the wording as explained in the main project brief.
Nice to have
• I want the flyer to be bold, eye-catching and modern.
• We particularly like the font Trebuchet MS for general copy but please feel free to use any other font for bolder, main titles.
Should not have
• We don't want anything gimmicky. No cheesy marketing.
• We only want professional looking designs. With the greatest of respect, if you're just starting out or don't really do design but think you'll use this as practise, please don't waste your or our time. We've previously run contests for other projects where we've had designs submitted that have clearly been done on MS Word and used Clipart and Wordart. That's really not what we are looking for.

```html
<!DOCTYPE html>
<html lang="en">
<head>
<meta charset="utf-8">
<title>Pelham Gardening Services – Lawn Treatment Flyer</title>
<link href="https://fonts.googleapis.com/css2?family=Oswald:wght@600;700&family=Nunito:ital,wght@0,700;1,900&family=PT+Sans:ital,wght@0,400;0,700;1,700&display=swap" rel="stylesheet">
<style>
:root{
  --purple:#7a3486;
  --purple-light:#a77db5;
  --green:#3cb54a;
  --green-pale:#c8e6b4;
  --green-mid:#8fd07a;
  --green-deep:#44b649;
  --ink:#2b2b2b;
  --bg:#000;
  --white:#fff;
}
*{box-sizing:border-box;margin:0;padding:0}
html,body{width:1200px;height:1000px;overflow:hidden;background:var(--bg)}
body{position:relative;font-family:"PT Sans",sans-serif}
.page{position:absolute;top:91px;width:577px;height:818px;background:var(--white);overflow:hidden}
.page--front{left:17px}
.page--back{left:607px}
.abs{position:absolute}

/* logo lockup */
.logo-card{position:absolute;top:0;background:var(--white);border:2px solid var(--purple);border-top:none;border-radius:0 0 26px 26px;display:flex;flex-direction:column;align-items:center;justify-content:center;gap:8px}
.logo-card .dot{width:26px;height:26px;border-radius:50%;background:var(--green)}
.logo-card .name{font-family:"PT Sans",sans-serif;font-weight:700;font-size:17px;line-height:1.15;color:var(--purple);text-align:center}

/* front */
.hero-photo{left:0;top:0;width:577px;height:270px;background:linear-gradient(180deg,#8fb06a 0%,#5f9a3a 35%,#cfc7b8 60%,#4f8f2c 100%)}
.hero-curve{left:0;top:180px}
.title{left:0;top:188px;width:577px;display:flex;justify-content:center;white-space:nowrap;font-family:"Oswald",sans-serif;font-weight:700;font-size:37px;line-height:48px;color:var(--white);letter-spacing:-.2px;text-shadow:2px 2px 0 var(--purple),-2px -2px 0 var(--purple),2px -2px 0 var(--purple),-2px 2px 0 var(--purple),0 3px 0 var(--purple),3px 0 0 var(--purple),0 -3px 0 var(--purple),-3px 0 0 var(--purple);transform:rotate(-6deg)}
.strapline{left:0;top:248px;width:577px;display:flex;justify-content:center;white-space:nowrap;font-family:"Nunito",sans-serif;font-style:italic;font-weight:900;font-size:24.5px;color:var(--green);transform:rotate(-5deg)}
.treatments{left:22px;top:326px;list-style:none}
.treatments li{display:flex;align-items:center;gap:10px;height:34.8px;font-family:"Nunito",sans-serif;font-weight:700;font-size:19px;color:var(--green)}
.leaf{width:16px;height:18px;flex:none}
.tile{width:145px;height:145px;border:3px solid var(--purple);border-radius:14px}
.tile--a{left:254px;top:317px;background:linear-gradient(160deg,#6f9a55,#3d8a2a)}
.tile--b{left:407px;top:317px;background:linear-gradient(160deg,#7aa06a,#4f8f36)}
.tile--c{left:254px;top:471px;background:linear-gradient(160deg,#b33a2c,#8f7a3a 50%,#b7a050)}
.tile--d{left:407px;top:471px;background:linear-gradient(160deg,#4e8a38,#5a4634)}
.select-note{left:0;top:632px;width:577px;text-align:center;font-family:"Nunito",sans-serif;font-weight:700;font-size:13.5px;line-height:18px;color:var(--green)}

/* footer */
.grass{left:0;top:678px;width:577px;height:110px;background:linear-gradient(180deg,rgba(255,255,255,0) 0%,#7ccd3e 35%,#2f9a25 100%)}
.footer-wave{left:0;top:690px}
.contact{left:0;top:772px;width:577px;height:43px;display:flex;justify-content:space-between;align-items:center;padding:0 20px;font-family:"Oswald",sans-serif;font-weight:700;color:var(--white)}
.contact .phone{display:flex;align-items:center;gap:6px;font-size:24px}
.contact .url{font-size:16px;letter-spacing:.3px}

/* back */
.back-photo{left:0;top:0;width:577px;height:225px;background:linear-gradient(180deg,#dfe6d8,#eef0e8 70%,#f6f6f2)}
.copy-top{left:27px;top:28px;width:523px;font-size:14.4px;line-height:18px;color:var(--ink);text-align:justify}
.copy-top .spacer{float:left;width:216px;height:106px}
.copy-top h2{font-style:italic;font-weight:700;font-size:16.5px;color:var(--purple);margin-bottom:2px;line-height:20px}
.copy-top b{color:var(--purple)}
.band{left:0;top:224px;width:577px;height:130px;background:var(--purple);padding:9px 27px 0;color:var(--white);font-size:14.4px;line-height:18px;text-align:justify}
.packages{left:27px;top:385px;border-collapse:separate;border-spacing:0;font-size:11px}
.packages th{height:18px;font-family:"Oswald",sans-serif;font-weight:600;font-size:11px;color:var(--ink);text-transform:uppercase;letter-spacing:.2px;border-right:3px solid var(--white)}
.packages td{height:23px;border-top:2px solid var(--white);border-right:3px solid var(--white);text-align:center}
.packages .col-std{background:var(--green-pale);width:130px}
.packages .col-enh{background:var(--green-mid);width:131px}
.packages .col-pre{background:var(--green-deep);width:131px}
.packages th.blank,.packages td.row-label{background:none;border-right:none;padding:0}
.row-label span{display:block;width:136px;height:20px;line-height:20px;background:var(--purple);color:var(--white);border-radius:0 8px 8px 0;text-align:center;font-size:11px}
.tick{width:15px;height:15px;vertical-align:middle}
.others{left:0;top:602px;width:577px;text-align:center;color:var(--ink);font-size:12px;line-height:15px}
.others h3{display:inline-block;font-weight:400;font-size:12px;border-bottom:2px solid var(--green);padding:0 2px 1px;margin-bottom:4px}
.others i{font-style:normal;color:var(--green);padding:0 2px}
</style>
</head>
<body>

<!-- FRONT -->
<section class="page page--front">
  <div class="abs hero-photo" role="img" aria-label="Curving stone path through a lush green lawn with shrubs"></div>
  <svg class="abs hero-curve" width="577" height="120" viewBox="0 0 577 120"><path d="M0 75 Q300 40 577 10 L577 120 L0 120Z" fill="#fff"/></svg>
  <div class="logo-card" style="left:20px;width:198px;height:114px"><span class="dot"></span><span class="name">Pelham<br>Gardening Services</span></div>
  <h1 class="abs title">EXPERT LAWN TREATMENT SERVICE</h1>
  <p class="abs strapline">Lawn care by your local gardening expert</p>

  <ul class="abs treatments">
    <li><svg class="leaf" viewBox="0 0 16 18"><path d="M2 17C3 9 7 3 15 1 14 9 10 14 3 15Z" fill="#7a3486"/></svg>Lawn Fertilising</li>
    <li><svg class="leaf" viewBox="0 0 16 18"><path d="M2 17C3 9 7 3 15 1 14 9 10 14 3 15Z" fill="#7a3486"/></svg>Scarification</li>
    <li><svg class="leaf" viewBox="0 0 16 18"><path d="M2 17C3 9 7 3 15 1 14 9 10 14 3 15Z" fill="#7a3486"/></svg>Aeration</li>
    <li><svg class="leaf" viewBox="0 0 16 18"><path d="M2 17C3 9 7 3 15 1 14 9 10 14 3 15Z" fill="#7a3486"/></svg>Weed Control</li>
    <li><svg class="leaf" viewBox="0 0 16 18"><path d="M2 17C3 9 7 3 15 1 14 9 10 14 3 15Z" fill="#7a3486"/></svg>Moss Control</li>
    <li><svg class="leaf" viewBox="0 0 16 18"><path d="M2 17C3 9 7 3 15 1 14 9 10 14 3 15Z" fill="#7a3486"/></svg>Hydration Booster</li>
    <li><svg class="leaf" viewBox="0 0 16 18"><path d="M2 17C3 9 7 3 15 1 14 9 10 14 3 15Z" fill="#7a3486"/></svg>Kempix</li>
    <li><svg class="leaf" viewBox="0 0 16 18"><path d="M2 17C3 9 7 3 15 1 14 9 10 14 3 15Z" fill="#7a3486"/></svg>Turfing &amp; Renovation</li>
  </ul>

  <div class="abs tile tile--a" role="img" aria-label="Freshly striped lawn behind a mower"></div>
  <div class="abs tile tile--b" role="img" aria-label="Gardener aerating a lawn"></div>
  <div class="abs tile tile--c" role="img" aria-label="Scarifier pulling thatch from grass"></div>
  <div class="abs tile tile--d" role="img" aria-label="Roll of new turf being laid"></div>

  <p class="abs select-note">Select a one-off treatment or choose from one<br>of our specially created lawn care packages.</p>

  <div class="abs grass" role="img" aria-label="Close-up band of green grass blades"></div>
  <svg class="abs footer-wave" width="577" height="128" viewBox="0 0 577 128"><path d="M0 20 Q290 70 577 20 L577 128 L0 128Z" fill="#a77db5"/><path d="M0 40 Q290 90 577 40 L577 128 L0 128Z" fill="#7a3486"/></svg>
  <div class="abs contact">
    <span class="phone"><svg width="16" height="20" viewBox="0 0 16 20"><path d="M4 1 7 5 5 8Q7 12 10 14L12 12 15 15 12 19Q2 16 1 4Z" fill="#fff"/></svg>01632 960481</span>
    <span class="url">WWW.PELHAMGARDENING.CO.UK/LAWNCARE</span>
  </div>
</section>

<!-- BACK -->
<section class="page page--back">
  <div class="abs back-photo" role="img" aria-label="Faded view of a garden patio and lawn"></div>
  <div class="logo-card" style="left:20px;width:206px;height:124px"><span class="dot"></span><span class="name">Pelham<br>Gardening Services</span></div>
  <div class="abs copy-top">
    <div class="spacer"></div>
    <h2>Passionate about Lawn Care</h2>
    As <b>expert</b> gardeners, we are <b>passionate</b> about horticulture and working to bring out the very best in your garden. When we work in your garden, we look at it and treat it with the same care and attention as if it were <b>our own</b>, before handing it back for you to enjoy. Our <b>passion</b> doesn’t end at just trees and shrubs though. Your grass is as much of a living, breathing plant as your shrubs and we therefore utilise our <b>expert</b> horticultural <b>knowledge</b> to ensure your lawn <b>thrives</b> and reaches its fullest <b>potential</b>.
  </div>
  <p class="abs band">Lawn care isn’t just about applying a fertiliser. It’s about really <b>understanding</b> your lawn and being able to use extensive <b>knowledge</b> and experience to diagnose and treat issues. It therefore stands to reason that you should employ an <b>expert</b> to bring out the best in your lawn which is why we at Pelham Gardening Services have created a <b>superior</b> lawn care service that will keep your lawn looking <b>lush, green</b> and <b>healthy</b> all year round.</p>

  <table class="abs packages">
    <thead><tr><th class="blank"></th><th class="col-std">Standard Package</th><th class="col-enh">Enhanced Package</th><th class="col-pre">Premium Package</th></tr></thead>
    <tbody>
      <tr><td class="row-label"><span>Spring Treatment</span></td><td class="col-std"><svg class="tick" viewBox="0 0 15 15"><path d="M2 8 6 12 13 2" fill="none" stroke="#7a3486" stroke-width="2.2"/></svg></td><td class="col-enh"><svg class="tick" viewBox="0 0 15 15"><circle cx="7.5" cy="7.5" r="7" fill="#d9c4e0"/><path d="M3 8 6.5 11 12 3" fill="none" stroke="#7a3486" stroke-width="2"/></svg></td><td class="col-pre"><svg class="tick" viewBox="0 0 15 15"><circle cx="7.5" cy="7.5" r="7" fill="#eee5f1"/><path d="M3 8 6.5 11 12 3" fill="none" stroke="#7a3486" stroke-width="2"/></svg></td></tr>
      <tr><td class="row-label"><span>Early Summer Treatment</span></td><td class="col-std"><svg class="tick" viewBox="0 0 15 15"><path d="M2 8 6 12 13 2" fill="none" stroke="#7a3486" stroke-width="2.2"/></svg></td><td class="col-enh"><svg class="tick" viewBox="0 0 15 15"><circle cx="7.5" cy="7.5" r="7" fill="#d9c4e0"/><path d="M3 8 6.5 11 12 3" fill="none" stroke="#7a3486" stroke-width="2"/></svg></td><td class="col-pre"><svg class="tick" viewBox="0 0 15 15"><circle cx="7.5" cy="7.5" r="7" fill="#eee5f1"/><path d="M3 8 6.5 11 12 3" fill="none" stroke="#7a3486" stroke-width="2"/></svg></td></tr>
      <tr><td class="row-label"><span>Late Summer Treatment</span></td><td class="col-std"><svg class="tick" viewBox="0 0 15 15"><path d="M2 8 6 12 13 2" fill="none" stroke="#7a3486" stroke-width="2.2"/></svg></td><td class="col-enh"><svg class="tick" viewBox="0 0 15 15"><circle cx="7.5" cy="7.5" r="7" fill="#d9c4e0"/><path d="M3 8 6.5 11 12 3" fill="none" stroke="#7a3486" stroke-width="2"/></svg></td><td class="col-pre"><svg class="tick" viewBox="0 0 15 15"><circle cx="7.5" cy="7.5" r="7" fill="#eee5f1"/><path d="M3 8 6.5 11 12 3" fill="none" stroke="#7a3486" stroke-width="2"/></svg></td></tr>
      <tr><td class="row-label"><span>Autumn/Winter Treatment</span></td><td class="col-std"><svg class="tick" viewBox="0 0 15 15"><path d="M2 8 6 12 13 2" fill="none" stroke="#7a3486" stroke-width="2.2"/></svg></td><td class="col-enh"><svg class="tick" viewBox="0 0 15 15"><circle cx="7.5" cy="7.5" r="7" fill="#d9c4e0"/><path d="M3 8 6.5 11 12 3" fill="none" stroke="#7a3486" stroke-width="2"/></svg></td><td class="col-pre"><svg class="tick" viewBox="0 0 15 15"><circle cx="7.5" cy="7.5" r="7" fill="#eee5f1"/><path d="M3 8 6.5 11 12 3" fill="none" stroke="#7a3486" stroke-width="2"/></svg></td></tr>
      <tr><td class="row-label"><span>Scarification</span></td><td class="col-std"></td><td class="col-enh"><svg class="tick" viewBox="0 0 15 15"><circle cx="7.5" cy="7.5" r="7" fill="#d9c4e0"/><path d="M3 8 6.5 11 12 3" fill="none" stroke="#7a3486" stroke-width="2"/></svg></td><td class="col-pre"><svg class="tick" viewBox="0 0 15 15"><circle cx="7.5" cy="7.5" r="7" fill="#eee5f1"/><path d="M3 8 6.5 11 12 3" fill="none" stroke="#7a3486" stroke-width="2"/></svg></td></tr>
      <tr><td class="row-label"><span>Aeration</span></td><td class="col-std"></td><td class="col-enh"><svg class="tick" viewBox="0 0 15 15"><circle cx="7.5" cy="7.5" r="7" fill="#d9c4e0"/><path d="M3 8 6.5 11 12 3" fill="none" stroke="#7a3486" stroke-width="2"/></svg></td><td class="col-pre"><svg class="tick" viewBox="0 0 15 15"><circle cx="7.5" cy="7.5" r="7" fill="#eee5f1"/><path d="M3 8 6.5 11 12 3" fill="none" stroke="#7a3486" stroke-width="2"/></svg></td></tr>
      <tr><td class="row-label"><span>Kempix Treatment</span></td><td class="col-std"></td><td class="col-enh"></td><td class="col-pre"><svg class="tick" viewBox="0 0 15 15"><circle cx="7.5" cy="7.5" r="7" fill="#eee5f1"/><path d="M3 8 6.5 11 12 3" fill="none" stroke="#7a3486" stroke-width="2"/></svg></td></tr>
      <tr><td class="row-label"><span>Hydration Boost Treatment</span></td><td class="col-std"></td><td class="col-enh"></td><td class="col-pre"><svg class="tick" viewBox="0 0 15 15"><circle cx="7.5" cy="7.5" r="7" fill="#eee5f1"/><path d="M3 8 6.5 11 12 3" fill="none" stroke="#7a3486" stroke-width="2"/></svg></td></tr>
    </tbody>
  </table>

  <div class="abs others">
    <h3>CHECK OUR OTHER GARDENING SERVICES:</h3><br>
    Lawn mowing <i>•</i> Shrub pruning <i>•</i> Hedge trimming <i>•</i> Weed killing<br>
    Garden clearance &amp; tidy-up <i>•</i> Planting &amp; design <i>•</i> Regular Garden Maintenance<br>
    Turfing <i>•</i> Fencing <i>•</i> Gutter clearance
  </div>

  <div class="abs grass" role="img" aria-label="Close-up band of green grass blades"></div>
  <svg class="abs footer-wave" width="577" height="128" viewBox="0 0 577 128"><path d="M0 20 Q290 70 577 20 L577 128 L0 128Z" fill="#a77db5"/><path d="M0 40 Q290 90 577 40 L577 128 L0 128Z" fill="#7a3486"/></svg>
  <div class="abs contact">
    <span class="phone"><svg width="16" height="20" viewBox="0 0 16 20"><path d="M4 1 7 5 5 8Q7 12 10 14L12 12 15 15 12 19Q2 16 1 4Z" fill="#fff"/></svg>01632 960481</span>
    <span class="url">WWW.PELHAMGARDENING.CO.UK/LAWNCARE</span>
  </div>
</section>

</body>
</html>
```